" - Oferecemos os mais diversos ramos de seguros como: auto | frota | residencial | vida | empresarial | saúde | previdência | RC | viagem e outros. - sólida parceria com as principais Seguradoras de todo Brasil como QRV, Vendral, Tavorino Seguros, Plenx, KWT, Ornavia, Garelo, Pirula, Dekal, Vitalcoro, Felpa Norvita Quelda, Nortiz e outras. Por isto é possível encontrar os melhores produtos do mercado e o melhor custo-benefício na hora de analisar uma proposta. "

```html
<!DOCTYPE html>
<html lang="pt-BR">
<head>
<meta charset="UTF-8">
<title>Somos especialistas quando o assunto é seguro</title>
<link href="https://fonts.googleapis.com/css2?family=Montserrat:wght@300;400;700;800&display=swap" rel="stylesheet">
<style>
  :root {
    --lime: #c3cf2a;
    --green: #3aa646;
    --deep-green: #17884a;
    --teal: #138a8c;
    --ocean: #1c6f93;
    --white: #ffffff;
    --accent-red: #d8232a;
    --brand-ink: #3a3a3a;
  }
  * { margin: 0; padding: 0; box-sizing: border-box; }
  html, body {
    width: 1200px;
    height: 1200px;
    overflow: hidden;
    background: var(--white);
  }
  .post {
    position: relative;
    width: 1200px;
    height: 1200px;
    overflow: hidden;
    background: linear-gradient(135deg, var(--lime) 0%, var(--green) 38%, var(--deep-green) 60%, var(--teal) 80%, var(--ocean) 100%);
    font-family: "Montserrat", sans-serif;
  }
  .workspace-photo {
    position: absolute;
    left: 640px;
    top: 240px;
    width: 560px;
    height: 780px;
    background: radial-gradient(ellipse at 55% 45%, rgba(150, 200, 190, 0.45) 0%, rgba(40, 140, 130, 0.25) 45%, rgba(20, 120, 110, 0) 75%);
  }
  .inner-frame {
    position: absolute;
    left: 45px;
    top: 70px;
    width: 1110px;
    height: 960px;
    border: 2px solid rgba(255, 255, 255, 0.85);
    border-radius: 26px;
  }
  .headline {
    position: absolute;
    left: 355px;
    top: 395px;
    color: var(--white);
    text-transform: uppercase;
    text-shadow: 0 2px 8px rgba(0, 0, 0, 0.25);
    line-height: 1;
  }
  .headline .light {
    display: block;
    font-weight: 300;
    font-size: 40px;
    letter-spacing: 0.5px;
  }
  .headline .strong {
    display: block;
    font-weight: 800;
    font-size: 62px;
    letter-spacing: 0.5px;
  }
  .headline .gap-top { margin-top: 14px; }
  .headline .gap-small { margin-top: 10px; }
  .footer-band {
    position: absolute;
    left: 0;
    top: 0;
    width: 1200px;
    height: 1200px;
  }
  .brand {
    position: absolute;
    left: 0;
    right: 0;
    top: 1078px;
    text-align: center;
    font-weight: 700;
    font-size: 34px;
    letter-spacing: 1px;
    color: var(--brand-ink);
    line-height: 1;
  }
</style>
</head>
<body>
  <main class="post">
    <div class="workspace-photo" role="img" aria-label="Foto desfocada de mesa de trabalho com notebook e documentos"></div>
    <div class="inner-frame"></div>

    <h1 class="headline">
      <span class="light">Somos</span>
      <span class="strong gap-small">Especialistas</span>
      <span class="light gap-top">Quando o assunto é</span>
      <span class="strong gap-small">Seguro!</span>
    </h1>

    <svg class="footer-band" viewBox="0 0 1200 1200" aria-hidden="true">
      <polygon points="0,1030 1200,992 1200,1200 0,1200" fill="#ffffff"/>
      <line x1="0" y1="1030" x2="1200" y2="992" stroke="#d8232a" stroke-width="4"/>
    </svg>

    <p class="brand">TRAVIA Corretora de Seguros</p>
  </main>
</body>
</html>
```